Small Business Consulting Firm Needs Business Card Design

Need a sleek modern business card with 2 sides matching the colors of our logo. We will be placing these with a mailer we are sending out. These business cards will only ever be given to business owners. We operate helping businesses who are struggling with cash flow or finances. If the green and blue design needs to be moved to the right of "Harborline Crest Consulting" for aesthetic purposes that is ok. We will need an editable file if possible. We would like to include the reps name, email, website, and phone number. For now just use Peter Vance, pvance@harborlinecrest.com, www.harborlinecrest.com, and 833-555-0172.

```html
<!DOCTYPE html>
<html lang="en">
<head>
<meta charset="utf-8">
<title>Harborline Crest Consulting – Business Card</title>
<link rel="stylesheet" href="https://fonts.googleapis.com/css2?family=Open+Sans:wght@400&family=Arimo:wght@400;700&display=swap">
<style>
  :root {
    --backdrop: #2a2a2a;
    --card: #f7f7f7;
    --card-edge: #e4e4e4;
    --brand-grey: #555a5e;
    --brand-green: #5e9b2e;
    --brand-blue: #1f74b8;
    --ink: #1e1e1e;
    --white: #ffffff;
  }
  * { box-sizing: border-box; margin: 0; padding: 0; }
  html, body {
    width: 1200px; height: 997px; overflow: hidden;
    background: var(--backdrop);
  }
  .sheet {
    width: 1200px; height: 997px;
    display: flex; align-items: center; justify-content: center; gap: 40px;
  }
  .card {
    position: relative;
    width: 540px; height: 310px;
    background: linear-gradient(160deg, var(--white), var(--card) 60%, var(--card-edge));
    border-radius: 16px;
    overflow: hidden;
    box-shadow: 0 18px 40px rgba(0,0,0,.55);
  }

  /* Brand lockup */
  .brand {
    display: flex; align-items: center; gap: 12px;
    color: var(--brand-grey);
    font-family: "Open Sans", sans-serif; font-weight: 400;
    text-transform: uppercase;
  }
  .brand-square { flex: none; background: var(--brand-green); }
  .brand-name { line-height: 1.15; }

  /* Logo side */
  .card--logo .brand { position: absolute; left: 60px; top: 50%; transform: translateY(-50%); }
  .card--logo .brand-square { width: 40px; height: 40px; }
  .card--logo .brand-name { font-size: 26px; letter-spacing: .5px; }
  .card--logo .brand-name small { display: block; font-size: 13px; letter-spacing: 6px; }

  /* Detail side */
  .card--detail .brand { position: absolute; right: 28px; top: 30px; }
  .card--detail .brand-square { width: 22px; height: 22px; }
  .card--detail .brand-name { font-size: 16px; text-align: right; }
  .card--detail .brand-name small { display: block; font-size: 9px; letter-spacing: 4px; }

  .person {
    position: absolute; left: 24px; right: 28px; top: 132px;
    font-family: "Arimo", sans-serif;
  }
  .person-name { color: var(--brand-green); font-weight: 700; font-size: 18px; letter-spacing: .5px; }
  .person-role-row { display: flex; align-items: center; gap: 8px; }
  .person-role { color: var(--brand-blue); font-weight: 700; font-size: 12px; flex: none; }
  .rule { flex: 1; height: 1.5px; background: var(--ink); }

  .contacts {
    position: absolute; left: 24px; top: 196px;
    list-style: none;
    font-family: "Arimo", sans-serif; font-size: 12.5px; color: var(--ink);
  }
  .contacts li { display: flex; align-items: center; gap: 9px; height: 20px; }
  .contacts svg { width: 14px; height: 14px; flex: none; }

  .office {
    position: absolute; right: 28px; top: 182px; text-align: right;
    font-family: "Arimo", sans-serif; font-size: 11.5px; color: var(--ink); line-height: 1.25;
  }
  .office-name { color: var(--brand-green); font-weight: 700; font-size: 12px; }

  .footer-bands { position: absolute; left: 0; bottom: 0; width: 540px; height: 50px; }
  .site {
    position: absolute; right: 26px; bottom: 20px;
    font-family: "Arimo", sans-serif; font-size: 12.5px; letter-spacing: 1.2px;
    color: var(--white);
  }
</style>
</head>
<body>
<main class="sheet">

  <section class="card card--logo" aria-label="Card front">
    <div class="brand">
      <span class="brand-square"></span>
      <span class="brand-name">Harborline Crest<small>Consulting</small></span>
    </div>
  </section>

  <section class="card card--detail" aria-label="Card back">
    <div class="brand">
      <span class="brand-name">Harborline Crest<small>Consulting</small></span>
      <span class="brand-square"></span>
    </div>

    <div class="person">
      <p class="person-name">CLARA WENDT</p>
      <div class="person-role-row">
        <p class="person-role">Founder</p>
        <span class="rule"></span>
      </div>
    </div>

    <ul class="contacts">
      <li>
        <svg viewBox="0 0 14 14" aria-hidden="true"><circle cx="7" cy="7" r="7" fill="var(--brand-blue)"/><path d="M4.2 4.3c.4-.5 1-.5 1.3 0l.6.9c.2.3.1.6-.1.8l-.4.3c.3.8.9 1.4 1.7 1.8l.3-.4c.2-.3.5-.3.8-.1l.9.6c.4.3.4.9 0 1.2-.6.6-1.5.7-2.3.3C5.6 9 4.6 8 4 6.7c-.3-.8-.3-1.700.2-2.4z" fill="#fff"/></svg>
        +34 600 55 0131
      </li>
      <li>
        <svg viewBox="0 0 14 14" aria-hidden="true"><circle cx="7" cy="7" r="7" fill="var(--brand-blue)"/><rect x="4.8" y="3.5" width="4.4" height="2" fill="#fff"/><rect x="3.5" y="5.8" width="7" height="3" rx=".6" fill="#fff"/><rect x="4.8" y="8.2" width="4.4" height="2.3" fill="#fff" stroke="var(--brand-blue)" stroke-width=".5"/></svg>
        +34 900 55 0148
      </li>
      <li>
        <svg viewBox="0 0 14 14" aria-hidden="true"><circle cx="7" cy="7" r="7" fill="var(--brand-blue)"/><rect x="3.6" y="4.6" width="6.8" height="4.8" fill="#fff"/><path d="M3.6 4.6 7 7.3l3.4-2.7" fill="none" stroke="var(--brand-blue)" stroke-width=".8"/></svg>
        care@harborlinecrest.com
      </li>
    </ul>

    <div class="office">
      <p class="office-name">HARBORLINE CREST</p>
      <p>14 Alder Row, Quay Street</p>
      <p>Canada</p>
    </div>

    <svg class="footer-bands" viewBox="0 0 540 50" aria-hidden="true">
      <path d="M0 30 L322 30 Q328 30 331 24 L333 20 L338 20 L335 28 Q331 36 322 36 L0 36 Z" fill="var(--brand-blue)"/>
      <path d="M0 39 L326 39 Q334 39 338 30 L344 16 Q348 6 360 6 L540 6 L540 50 L0 50 Z" fill="var(--brand-green)"/>
    </svg>
    <p class="site">www.harborlinecrest.com</p>
  </section>

</main>
</body>
</html>
```